Image Broschüre für Veranstaltungstechnik
Zielgruppe
Veranstaltungstechnik
Aufgabenstellung
Modernes aber seriöses Image Produkt, um per Print Werbung an Firmen in der Region zu versenden.
Ich habe das Format geändert in ein kleines Image Book und das Preisgeld dafür deutlich angehoben :)
Daher wäre die aktuelle Version ein kleines „Buch“ im A5 Format, mir ein paar Seiten. Dazu könnte man mit ein Grunddesign mit 2 Seiten oder so vorstellen und dazu die Information geben, wie viele „einfache“ Seiten dieses dann beinhalten würde. Ich denke so an ca 10/15 Seiten wobei das Design sich nicht grundlegend verändern wird. Die Inhalte werden wir dann natürlich liefern
Das ganze sollte dem professionellen Anspruch einer Mittelständigen bis großen Firma entsprechen, welche in erster Linie die Empfänger dieser Inage Broschüre sein sollen. Ausserdem sollte eine kleine Variante erstellt werden ( nur Titelseite evtl etwas abgeändert ), welche auch an Interessierte Firmen als PDF versendet werden kann.
Webseite: www.mv-buehnenlicht-beispiel.de
Weitere Projekte im Bereich Corporate Design und erstellen von Aktionsflyern für bestimmte Events folgen mit Sicherheit.

```html
<!DOCTYPE html>
<html lang="de">
<head>
<meta charset="utf-8">
<title>MV Bühnenlicht – Imagebroschüre</title>
<link rel="stylesheet" href="https://fonts.googleapis.com/css2?family=Montserrat:wght@800&family=Open+Sans:wght@400;600&display=swap">
<style>
  :root {
    --backdrop: #e6e6ea;
    --paper: #f6f6f7;
    --navy: #1b1f4a;
    --blue: #2b41a8;
    --deep: #0d1657;
    --teal: #4fc3b9;
    --band: #d8dbe8;
    --text: #4a4d5c;
  }
  * { margin: 0; padding: 0; box-sizing: border-box; }
  html, body { width: 1200px; height: 2400px; overflow: hidden; }
  body {
    background: var(--backdrop);
    font-family: "Open Sans", sans-serif;
    color: var(--text);
    position: relative;
  }
  .sheet {
    position: absolute;
    left: 100px;
    display: flex;
    box-shadow: 0 18px 40px rgba(0,0,0,.12);
  }
  .sheet--cover { left: 350px; top: 70px; }
  .sheet--inside { top: 847px; }
  .sheet--outside { top: 1624px; }
  .page {
    position: relative;
    width: 500px;
    height: 707px;
    background: var(--paper);
    overflow: hidden;
  }
  .page + .page { border-left: 1px solid #dcdce0; }

  .headline {
    font-family: "Montserrat", sans-serif;
    font-weight: 800;
    color: var(--navy);
    letter-spacing: .12em;
    text-transform: uppercase;
    line-height: 1.3;
  }
  .rule { height: 2px; background: var(--navy); }
  .photo { position: absolute; }
  .band { position: absolute; background: var(--band); }

  /* cover */
  .cover__band-top { left: 0; top: 40px; width: 170px; height: 110px; }
  .cover__stage {
    left: 0; top: 150px; width: 500px; height: 390px;
    background: radial-gradient(circle at 40% 70%, #c9d6ff 0, #5a78e0 22%, var(--blue) 45%, var(--deep) 100%);
  }
  .cover__band-bottom { left: 0; top: 540px; width: 500px; height: 16px; }
  .cover__circle { border-radius: 50%; border: 5px solid #fff; }
  .cover__circle--venue { left: 250px; top: 20px; width: 160px; height: 160px;
    background: radial-gradient(circle at 50% 40%, #e08bc4, #7b3a8c 60%, #2b1a55); }
  .cover__circle--stage { left: 130px; top: 150px; width: 130px; height: 130px;
    background: radial-gradient(circle at 50% 50%, #d7e4ff, #4a6fd1 55%, #1a2466); }
  .cover__circle--dinner { left: 300px; top: 165px; width: 140px; height: 140px;
    background: radial-gradient(circle at 50% 60%, #f7e2c8, #e8b274 45%, #c9c3bd); }
  .cover__brand-disc {
    position: absolute; left: 40px; top: 330px; width: 250px; height: 250px;
    border-radius: 50%;
    background: rgba(235, 240, 255, .6);
  }
  .brand {
    position: absolute; left: 68px; top: 425px;
    display: flex; align-items: center; gap: 10px;
  }
  .brand__dot { width: 16px; height: 16px; border-radius: 50%; background: var(--teal); }
  .brand__name {
    font-family: "Montserrat", sans-serif; font-weight: 800;
    font-size: 24px; color: var(--navy); letter-spacing: .02em;
  }
  .cover__headline {
    position: absolute; left: 0; right: 0; top: 592px;
    text-align: center; font-size: 18px;
  }
  .cover__rule { position: absolute; left: 175px; width: 150px; top: 665px; }

  /* inside left */
  .intro__photo {
    left: 0; top: 0; width: 500px; height: 250px;
    background: linear-gradient(160deg, #1a1f6e 0%, #3346b8 45%, #8aa6ff 70%, #1b237a 100%);
  }
  .intro__band { left: 0; top: 250px; width: 500px; height: 14px; }
  .intro__headline { position: absolute; left: 50px; right: 50px; top: 296px; font-size: 17px; }
  .intro__rule { position: absolute; left: 50px; width: 120px; top: 370px; }
  .body-copy { font-size: 13px; line-height: 1.75; text-align: justify; }
  .intro__copy { position: absolute; left: 50px; right: 50px; top: 400px; }

  /* inside right */
  .service__headline { position: absolute; left: 50px; right: 50px; top: 40px; font-size: 17px; }
  .service__band { left: 0; top: 112px; width: 500px; height: 14px; }
  .service__photo {
    left: 0; top: 126px; width: 500px; height: 210px;
    background: linear-gradient(200deg, #121a66 0%, #2f44b4 50%, #9cb8ff 68%, #1a2478 100%);
  }
  .service__copy { position: absolute; left: 50px; right: 50px; top: 360px; }
  .service__copy .body-copy { font-size: 12.5px; line-height: 1.65; }
  .service__cta { margin-top: 12px; font-size: 12.5px; line-height: 1.65; }
  .service__footer {
    position: absolute; left: 50px; right: 50px; bottom: 30px;
    text-align: center;
  }
  .service__mail { font-size: 12px; font-style: italic; letter-spacing: .08em; }
  .service__web { margin-top: 8px; font-size: 14px; }

  /* back */
  .back__photo {
    left: 0; top: 0; width: 500px; height: 300px;
    background: linear-gradient(180deg, #6b6f78 0%, #b9bcc4 45%, #eef0f4 70%, #8a8e97 100%);
  }
  .back__band { left: 0; top: 300px; width: 500px; height: 40px; }
  .imprint { position: absolute; left: 0; right: 0; top: 470px; text-align: center; font-style: normal; }
  .imprint__line { font-family: "Montserrat", sans-serif; font-weight: 800; font-size: 11px; letter-spacing: .14em; color: var(--navy); text-transform: uppercase; line-height: 2.1; }
  .imprint__web { margin-top: 14px; font-size: 15px; }
</style>
</head>
<body>

<section class="sheet sheet--cover" aria-label="Titelseite">
  <article class="page cover">
    <div class="band cover__band-top"></div>
    <div class="photo cover__stage" role="img" aria-label="Bühne mit blauem Licht und Lichtstrahlen"></div>
    <div class="band cover__band-bottom"></div>
    <div class="photo cover__circle cover__circle--venue" role="img" aria-label="Farbig beleuchtetes Schloss bei Nacht"></div>
    <div class="photo cover__circle cover__circle--stage" role="img" aria-label="Konferenzsaal mit Leinwand"></div>
    <div class="photo cover__circle cover__circle--dinner" role="img" aria-label="Festlich gedeckte Gala-Tafel"></div>
    <div class="cover__brand-disc"></div>
    <div class="brand"><span class="brand__dot"></span><span class="brand__name">MV Bühnenlicht</span></div>
    <h1 class="headline cover__headline">Ihr Partner für Medien-,<br>Licht- und Tontechnik</h1>
    <div class="rule cover__rule"></div>
  </article>
</section>

<section class="sheet sheet--inside" aria-label="Innenseiten">
  <article class="page intro">
    <div class="photo intro__photo" role="img" aria-label="Traversen mit Scheinwerfern in blauem Licht"></div>
    <div class="band intro__band"></div>
    <h2 class="headline intro__headline">MV Eventtechnik – der Partner<br>für Ihr Firmenevent</h2>
    <div class="rule intro__rule"></div>
    <p class="body-copy intro__copy">MV Bühnenlicht GmbH &amp; Co. KG ist ein Full-Service Anbieter für Medientechnik sowie Licht- und Tontechnik. Bereits im Jahr 2002 gegründet, verstehen wir uns seit Jahren als ein professioneller und zuverlässiger Partner bei der Durchführung von hochwertigen Veranstaltungen. Neben unseren Firmenkonferenzen und Messen betreuen wir Galas, Konzerte und Produktpräsentationen mit aktuellem Equipment. Ob Beschallung, Bühnenlicht, LED-Leinwände, Beamer oder Videoproduktion – bei uns steht die Qualität der Technik immer im Vordergrund.</p>
  </article>
  <article class="page service">
    <h2 class="headline service__headline">Beratung | Konzeption | Technik<br>– alles aus einer Hand</h2>
    <div class="band service__band"></div>
    <div class="photo service__photo" role="img" aria-label="Veranstaltungshalle mit Lichttechnik in blauem Licht"></div>
    <div class="service__copy">
      <p class="body-copy">Wir planen gemeinsam mit unseren Kunden das Event vom ersten Brainstorming an und sind während des kompletten Prozesses für sie der Ansprechpartner, der gewerkeübergreifend alles im Blick behält und seine jahrelangen Erfahrungen einbringt. Durch unseren Standort in Musterbach sind wir mit unserem gesamten Team aus erfahrenen Projektmanagern und Technikern in der ganzen Region vertreten. Gerne unterbreiten wir Ihnen ein unverbindliches Angebot und stehen Ihnen jederzeit für alle Fragen zur Verfügung.</p>
      <p class="service__cta">Fragen Sie uns! Wir haben für jeden Anspruch die richtige Lösung parat.</p>
    </div>
    <div class="service__footer">
      <p class="service__mail">info@mv-buehnenlicht-beispiel.de</p>
      <p class="headline service__web">MV-BUEHNENLICHT-BEISPIEL.DE</p>
    </div>
  </article>
</section>

<section class="sheet sheet--outside" aria-label="Rückseite und Titelseite">
  <article class="page back">
    <div class="photo back__photo" role="img" aria-label="Traversenkonstruktion mit Scheinwerfern"></div>
    <div class="band back__band"></div>
    <address class="imprint">
      <p class="imprint__line">MV Bühnenlicht GmbH &amp; Co. KG</p>
      <p class="imprint__line">Lindenstraße 12 | 70000 Musterbach</p>
      <p class="imprint__line">+49 (0)7000-123456-0</p>
      <p class="headline imprint__web">MV-BUEHNENLICHT-BEISPIEL.DE</p>
    </address>
  </article>
  <article class="page cover">
    <div class="band cover__band-top"></div>
    <div class="photo cover__stage" role="img" aria-label="Bühne mit blauem Licht und Lichtstrahlen"></div>
    <div class="band cover__band-bottom"></div>
    <div class="photo cover__circle cover__circle--venue" role="img" aria-label="Farbig beleuchtetes Schloss bei Nacht"></div>
    <div class="photo cover__circle cover__circle--stage" role="img" aria-label="Konferenzsaal mit Leinwand"></div>
    <div class="photo cover__circle cover__circle--dinner" role="img" aria-label="Festlich gedeckte Gala-Tafel"></div>
    <div class="cover__brand-disc"></div>
    <div class="brand"><span class="brand__dot"></span><span class="brand__name">MV Bühnenlicht</span></div>
    <h2 class="headline cover__headline">Ihr Partner für Medien-,<br>Licht- und Tontechnik</h2>
    <div class="rule cover__rule"></div>
  </article>
</section>

</body>
</html>
```